New Business Card for Casual Beachfront Cafe

Quirky Beachfront Cafe at Moana, South Australia needs a DOUBLE SIDED business card to print on PrintHarbor.

Target Market(s)

Business Cards sit on the counter for Guests to take with them. Please view our website www.saltreefcafe.com.au to get a feel for the Cafe. You may also view our Instagram at @saltreefcafe

Industry/Entity Type

Cafe / Restaurant

Contact Information for Business Card

Information equivalent to: Breakfast, Lunch, Dinner, Coffee, Takeaway / 117 Parade Moana SA 5169 / Menu & Opening Hours: www.saltreefcafe.com.au / ph (08) 8461 9273

Requirements
Must have
• Information equivalent to: Breakfast, Lunch, Dinner, Coffee, Takeaway / 117 Parade Moana SA 5169 / Menu & Opening Hours: www.saltreefcafe.com.au / ph (08) 8461 9273
Nice to have
• Potentially some of our trademark colours (Cafe can be searched via Seekly)
Should not have
• Must NOT have image of the building. May have the logo provided on one side but not necessarily, depending on how you wish to design the card

```html
<!DOCTYPE html>
<html lang="en">
<head>
<meta charset="utf-8">
<title>Salt Reef Cafe – Business Card</title>
<link href="https://fonts.googleapis.com/css2?family=Arvo:wght@400;700&family=Zilla+Slab:wght@400&display=swap" rel="stylesheet">
<style>
  :root {
    --page: #ffffff;
    --card: #1f1e22;
    --yellow: #f7c300;
    --white: #ffffff;
    --text-soft: #f1f1f1;
    --photo-dark: #3b3735;
    --photo-warm: #5b4638;
  }
  * { box-sizing: border-box; margin: 0; padding: 0; }
  html, body { width: 1200px; height: 900px; overflow: hidden; background: var(--page); }
  .canvas { position: relative; width: 1200px; height: 900px; }
  .card {
    position: absolute; top: 51px; width: 532px; height: 797px;
    background: var(--card); overflow: hidden;
    font-family: "Arvo", Georgia, serif;
  }
  .card--front { left: 54px; }
  .card--back { left: 614px; }
  .swoosh { position: absolute; left: 0; top: 0; width: 532px; height: 797px; }

  .photo {
    position: absolute; border-radius: 28px;
    background: linear-gradient(160deg, var(--photo-dark), var(--photo-warm));
  }
  .photo--faint { opacity: .14; }

  .front-kicker {
    position: absolute; top: 14px; width: 100%; text-align: center;
    color: var(--white); font-size: 31px; font-weight: 700; letter-spacing: .5px;
  }
  .brand-name {
    position: absolute; display: flex; align-items: center; justify-content: center;
    text-align: center; color: var(--white); font-weight: 700; line-height: 1.05;
  }
  .card--front .brand-name { left: 123px; top: 62px; width: 286px; height: 148px; font-size: 44px; }
  .card--back .brand-name { left: 325px; top: 44px; width: 168px; height: 86px; font-size: 25px; }
  .front-invite {
    position: absolute; top: 224px; width: 100%; text-align: center;
    color: var(--white); font-size: 25px; font-weight: 700;
  }
  .rule { position: absolute; height: 2px; background: var(--yellow); }
  .card--front .rule { left: 48px; top: 272px; width: 443px; transform: rotate(-.35deg); }
  .card--back .rule { left: 32px; top: 322px; width: 277px; transform: rotate(-.3deg); }
  .hours { position: absolute; left: 48px; top: 303px; list-style: none; }
  .hours li { color: var(--yellow); font-size: 19px; font-weight: 700; line-height: 26.3px; }
  .hours .day { margin-right: 6px; }
  .front-address {
    position: absolute; right: 20px; top: 737px;
    color: var(--yellow); font-size: 21.5px; font-weight: 700;
  }
  .meals {
    position: absolute; left: 36px; top: 226px;
    color: var(--white); font-size: 30px; font-weight: 700; line-height: 44px;
  }
  .contact { position: absolute; list-style: none; }
  .contact li {
    display: flex; align-items: center; gap: 9px;
    color: var(--text-soft); font-family: "Zilla Slab", Georgia, serif; font-size: 20.5px;
    height: 37.5px;
  }
  .contact--primary { left: 44px; top: 362px; }
  .contact--online { left: 250px; top: 446px; }
  .contact .icon { width: 30px; height: 20px; flex: none; }
</style>
</head>
<body>
<main class="canvas">

  <section class="card card--front">
    <div class="photo photo--faint" role="img" aria-label="Faded photo of a frying pan with fried egg, bacon and spatula" style="left:118px; top:272px; width:345px; height:300px;"></div>

    <svg class="swoosh" viewBox="0 0 532 797" aria-hidden="true">
      <path d="M200 555 C 320 500, 430 470, 532 510" fill="none" stroke="var(--yellow)" stroke-width="14" stroke-linecap="round"/>
      <path d="M0 782 C 130 786, 260 750, 340 690 C 410 640, 470 620, 532 640" fill="none" stroke="var(--yellow)" stroke-width="11"/>
    </svg>

    <p class="front-kicker">THE BEST</p>
    <p class="brand-name">SALT REEF<br>CAFE</p>
    <p class="front-invite">COME TO VISIT US !</p>
    <div class="rule"></div>

    <ul class="hours">
      <li><span class="day">Mon</span>Closed</li>
      <li><span class="day">Tues</span>Closed</li>
      <li><span class="day">Wed</span>9am-2pm, 5pm-8pm</li>
      <li><span class="day">Thur</span>9am-2pm, 5pm-8pm</li>
      <li><span class="day">Fri</span>9am-2pm, 5pm-8pm</li>
      <li><span class="day">Sat</span>8:30am-8pm</li>
      <li><span class="day">Sun</span>8:30am-8pm</li>
    </ul>

    <div class="photo" role="img" aria-label="Photo of a black coffee cup on a white saucer with coffee beans" style="left:0; top:508px; width:270px; height:192px;"></div>
    <div class="photo" role="img" aria-label="Scattered roasted coffee beans" style="left:238px; top:639px; width:180px; height:90px;"></div>

    <p class="front-address">117 Parade Moana SA 5169</p>
  </section>

  <section class="card card--back">
    <svg class="swoosh" viewBox="0 0 532 797" aria-hidden="true">
      <path d="M0 48 C 120 20, 230 70, 300 150 C 370 225, 440 240, 532 205" fill="none" stroke="var(--yellow)" stroke-width="14"/>
      <path d="M0 613 C 60 612, 90 600, 120 610" fill="none" stroke="var(--yellow)" stroke-width="12"/>
      <path d="M300 720 C 380 775, 460 790, 532 775" fill="none" stroke="var(--yellow)" stroke-width="14"/>
      <path d="M470 250 L 515 285" stroke="var(--yellow)" stroke-width="2"/>
    </svg>

    <p class="brand-name">SALT REEF<br>CAFE</p>

    <p class="meals">BREAKFAST, LUNCH,<br>DINNER, COFFEE</p>
    <div class="rule"></div>

    <ul class="contact contact--primary">
      <li>
        <svg class="icon" viewBox="0 0 30 20" aria-hidden="true"><path d="M2 17 C 4 9, 10 6, 18 6 L18 1 L28 9 L18 17 L18 12 C 11 12, 6 13, 2 17 Z" fill="none" stroke="var(--yellow)" stroke-width="2" stroke-linejoin="round"/></svg>
        (08) 8461 9273
      </li>
      <li>
        <svg class="icon" viewBox="0 0 30 20" aria-hidden="true"><path d="M2 17 C 4 9, 10 6, 18 6 L18 1 L28 9 L18 17 L18 12 C 11 12, 6 13, 2 17 Z" fill="none" stroke="var(--yellow)" stroke-width="2" stroke-linejoin="round"/></svg>
        117 Parade Moana SA 5169
      </li>
    </ul>

    <ul class="contact contact--online">
      <li>
        <svg class="icon" viewBox="0 0 30 20" aria-hidden="true"><path d="M2 17 C 4 9, 10 6, 18 6 L18 1 L28 9 L18 17 L18 12 C 11 12, 6 13, 2 17 Z" fill="none" stroke="var(--yellow)" stroke-width="2" stroke-linejoin="round"/></svg>
        www.saltreefcafe.com.au
      </li>
      <li>
        <svg class="icon" viewBox="0 0 30 20" aria-hidden="true"><path d="M2 17 C 4 9, 10 6, 18 6 L18 1 L28 9 L18 17 L18 12 C 11 12, 6 13, 2 17 Z" fill="none" stroke="var(--yellow)" stroke-width="2" stroke-linejoin="round"/></svg>
        at @saltreefcafe
      </li>
    </ul>

    <div class="photo" role="img" aria-label="Photo of a black coffee cup on a white saucer with coffee beans" style="left:8px; top:556px; width:282px; height:207px;"></div>
    <div class="photo" role="img" aria-label="Scattered roasted coffee beans" style="left:260px; top:691px; width:176px; height:83px;"></div>
    <div class="photo" role="img" aria-label="Photo of a frying pan with fried egg, bacon and wooden spatula" style="left:346px; top:564px; width:165px; height:161px;"></div>
  </section>

</main>
</body>
</html>
```